K7 Digital Stationery Design Project

We are looking to have stationary designs created for our company branding materials. We are looking for the following to be created.
1. Business Cards (front & back)
2. Letterhead
3. Envelopes #10
We are a new web design, development and marketing firm. Primary color scheme is desired to be blue/grey/white. This web start-up is owned and operated by individuals with 15+ years experience each in the industry so should not look as though it is a start-up by young/inexperienced individuals.
We build website & custom applications/software. In addition we provide the full spectrum of web marketing solutions including SEO, PPC, Social Media, Branding, Content Marketing and PR.
Please let us know if you have any questions. Looking forward to seeing all the amazing design ideas.
Attached is our logo.
Thanks!
Target Market(s)
Company will be nearly 100% business to business sales. Looking to work with companies that are already established, with a website, who want to take their website and/or online marketing efforts to the next level.
Industry/Entity Type
Marketing
Look and feel

```html
<!DOCTYPE html>
<html lang="en">
<head>
<meta charset="utf-8">
<title>K7 Digital Stationery</title>
<link href="https://fonts.googleapis.com/css2?family=Jost:wght@300;400;600&family=Marcellus&display=swap" rel="stylesheet">
<style>
  :root {
    --ink: #4a4a4a;
    --grey: #9a9b9d;
    --logo-grey: #6d6e70;
    --blue: #0f86c6;
    --blue-light: #00aedb;
    --blue-deep: #0f6fb8;
    --paper: #ffffff;
    --edge: #d2d2d2;
    --card-dark: #0c0c0c;
  }
  html, body { margin: 0; padding: 0; overflow: hidden; }
  body {
    width: 1200px; height: 893px; position: relative;
    background: var(--paper);
    font-family: "Jost", sans-serif; font-weight: 300; color: var(--grey);
  }
  .section-title {
    position: absolute; margin: 0;
    font-family: "Marcellus", serif; font-weight: 400;
    font-size: 15px; color: var(--ink); letter-spacing: .3px;
  }
  .side-label {
    position: absolute; margin: 0;
    font-family: "Marcellus", serif; font-size: 11.5px; color: var(--ink);
  }
  .sheet {
    position: absolute; background: var(--paper);
    border: 1px solid var(--edge); box-sizing: border-box;
    box-shadow: 0 8px 6px -6px rgba(0,0,0,.28);
  }
  .brand { position: absolute; display: flex; align-items: center; gap: 4px; }
  .brand-dot { border-radius: 50%; background: var(--blue); flex: none; }
  .brand-name { font-weight: 600; color: var(--logo-grey); letter-spacing: .2px; white-space: nowrap; }
  .brand--small .brand-dot { width: 11px; height: 11px; }
  .brand--small .brand-name { font-size: 11px; }
  .brand--tiny .brand-dot { width: 9px; height: 9px; }
  .brand--tiny .brand-name { font-size: 9px; }
  .brand--large .brand-dot { width: 16px; height: 16px; }
  .brand--large .brand-name { font-size: 17px; color: #ffffff; }

  .tiny { position: absolute; font-size: 5.6px; line-height: 8px; white-space: nowrap; }
  .tiny .key { color: var(--blue); display: inline-block; width: 9px; }
  .link { color: var(--blue); }

  .letterhead { left: 46px; top: 73px; width: 487px; height: 689px; }

  .card-front {
    left: 605px; top: 73px; width: 271px; height: 166px;
    background: radial-gradient(ellipse at 50% 45%, #2d2d2d 0%, #161616 45%, var(--card-dark) 100%);
    border: none;
  }
  .card-front .brand { left: 50%; top: 50%; transform: translate(-50%, -50%); }
  .card-back { left: 899px; top: 73px; width: 271px; height: 166px; }
  .card-name { position: absolute; left: 16px; top: 62px; font-size: 10.5px; color: var(--grey); margin: 0; font-weight: 300; }
  .card-role { position: absolute; left: 16px; top: 76px; font-size: 8.5px; color: var(--blue); margin: 0; font-weight: 400; }
  .card-back .tiny { font-size: 6.3px; line-height: 9.4px; }

  .envelope-front { left: 605px; top: 295px; width: 509px; height: 255px; }
  .envelope-back { left: 605px; top: 584px; width: 509px; height: 255px; overflow: hidden; }
  .envelope-flap {
    position: absolute; left: 0; top: 0; width: 100%; height: 127px;
    background: linear-gradient(to bottom, var(--blue-light), var(--blue-deep));
  }
</style>
</head>
<body>

  <h2 class="section-title" style="left:46px; top:42px;">A4 LETTERHEAD</h2>
  <h2 class="section-title" style="left:609px; top:42px;">BUSINESS CARD</h2>
  <h2 class="section-title" style="left:605px; top:258px;">DL ENVELOPE</h2>
  <p class="side-label" style="left:612px; top:274px;">Front</p>
  <p class="side-label" style="left:612px; top:566px;">Back</p>

  <section class="sheet letterhead">
    <div class="brand brand--small" style="left:34px; top:80px;">
      <span class="brand-dot"></span><span class="brand-name">K7 DIGITAL</span>
    </div>
    <div class="tiny" style="left:290px; top:50px;">
      address Lorem ipsum<br>dolor amet,consectetur<br>adipisicing elit.
    </div>
    <div class="tiny link" style="left:290px; top:93px;">k7digital.com</div>
    <div class="tiny" style="left:398px; top:50px;">
      <span class="key">U</span>044 555-010-010<br>
      <span class="key">T</span>044 5550123<br>
      <span class="key">M</span>0711 5550145<br>
      <span class="key">F</span>044 35550167
    </div>
  </section>

  <section class="sheet card-front">
    <div class="brand brand--large">
      <span class="brand-dot"></span><span class="brand-name">K7 DIGITAL</span>
    </div>
  </section>

  <section class="sheet card-back">
    <div class="brand brand--tiny" style="left:176px; top:48px;">
      <span class="brand-dot"></span><span class="brand-name">K7 DIGITAL</span>
    </div>
    <p class="card-name">Daniel Mercer</p>
    <p class="card-role">Designation</p>
    <div class="tiny" style="left:16px; top:97px;">
      Suite 12, Block C<br>Harbor Point Tower<br>Westgate Avenue<br>Brookfield-Canada
    </div>
    <div class="tiny" style="left:123px; top:97px;">
      <span class="key" style="width:13px;">U</span>000 555-222-333<br>
      <span class="key" style="width:13px;">T</span>000 5550123<br>
      <span class="key" style="width:13px;">M</span>000 5550145<br>
      <span class="key" style="width:13px;">F</span>000 5550167
    </div>
    <div class="tiny link" style="left:136px; top:141px;">daniel.mercer@k7digital.com<br>k7digital.com</div>
  </section>

  <section class="sheet envelope-front">
    <div class="brand brand--small" style="left:33px; top:76px;">
      <span class="brand-dot"></span><span class="brand-name">K7 DIGITAL</span>
    </div>
  </section>

  <section class="sheet envelope-back">
    <div class="envelope-flap"></div>
    <div class="tiny" style="left:33px; top:231px;">
      <span class="link">If undelivered, please return to</span><br>
      address Lorem ipsum dolor amet,consectetur adipisicing elit.
    </div>
  </section>

</body>
</html>
```